Dishcart

App Design for a an application on which you can order take aways from restaurants close to you.
(similar app : https://appvault.example/lu/app/brunomeal-pizza-burger-sushi/id538216047?l=en&mt=8 )

Logo is a taxi (psd of taxi an font attached)

Attached a draft mockup showing the screens needed.

Screens needed :

1. Splash Screen
2. Select you restaurant screen
3. Select your dish (meat, pizza, pasta....)
4. Select your extras (exta cheese, garlik etc...)
5. Exit screen with total amount and confirmation
6. Subscribe Screen where people have to register the first time.

Target Market(s)

age 14-54

Industry/Entity Type

Restaurant

Requirements
Must have
• Wood elements

```html
<!DOCTYPE html>
<html lang="fr">
<head>
<meta charset="utf-8">
<title>Dishcart – Restaurants</title>
<link href="https://fonts.googleapis.com/css2?family=Arimo:ital,wght@0,400;0,700;1,400&display=swap" rel="stylesheet">
<style>
  :root {
    --page-bg: #e9e9e9;
    --wood-dark: #2a140a;
    --wood-mid: #4a2614;
    --wood-light: #6b3a1f;
    --ribbon-light: #c88f58;
    --ribbon-dark: #8f5a2e;
    --ribbon-text: #ffffff;
    --ribbon-sub: #f3c9a1;
    --tab-silver-top: #f4f4f4;
    --tab-silver-bottom: #c9c9c9;
    --tab-text: #333333;
    --play-bg: #3b2a20;
    --bar-orange: #c97a2e;
    --bar-orange-dark: #8b4a18;
    --nav-tab: #6e4635;
    --nav-tab-dark: #4e3022;
    --panel-bg: rgba(120, 80, 55, 0.55);
    --panel-text: #f5ede6;
    --divider: #c9742f;
  }
  * { box-sizing: border-box; margin: 0; padding: 0; }
  html, body { width: 1200px; height: 1000px; overflow: hidden; }
  body {
    background: var(--page-bg);
    font-family: "Arimo", Arial, sans-serif;
    position: relative;
  }
  .app-screen {
    position: absolute;
    left: 285px; top: 32px;
    width: 630px; height: 935px;
    overflow: hidden;
    background: linear-gradient(90deg, var(--wood-dark), var(--wood-mid) 30%, #3a1d0e 60%, var(--wood-dark));
  }

  /* Header */
  .header {
    position: absolute; left: 0; top: 0; width: 630px; height: 220px;
    background: linear-gradient(90deg, #3a1c0c, var(--wood-light) 25%, #5a2f16 50%, var(--wood-light) 75%, #3a1c0c);
    border-bottom: 3px solid #e8e8e8;
  }
  .status-bar {
    height: 33px; display: flex; align-items: center; justify-content: space-between;
    padding: 0 14px;
    background: rgba(0, 0, 0, 0.15);
  }
  .range-panel {
    position: absolute; left: 35px; top: 90px; width: 390px; height: 78px;
    border-radius: 14px; background: var(--panel-bg);
    box-shadow: inset 0 1px 3px rgba(0,0,0,0.5), 0 1px 0 rgba(255,255,255,0.2);
    padding: 12px 22px 0;
  }
  .range-label { color: var(--panel-text); font-size: 16px; text-align: center; }
  .range-track {
    position: relative; margin-top: 18px; height: 5px; border-radius: 3px;
    background: #2d1a10; box-shadow: 0 1px 0 rgba(255,255,255,0.25);
  }
  .range-thumb {
    position: absolute; right: 0; top: -10px; width: 25px; height: 25px; border-radius: 50%;
    background: radial-gradient(circle at 40% 35%, #ffffff, #cfcfcf);
    box-shadow: 0 2px 3px rgba(0,0,0,0.5);
  }
  .brand {
    position: absolute; left: 470px; top: 70px; width: 140px; height: 140px;
    display: flex; flex-direction: column; align-items: center; justify-content: center; gap: 8px;
  }
  .brand-dot { width: 58px; height: 58px; border-radius: 50%; background: var(--bar-orange); }
  .brand-name { color: var(--panel-text); font-weight: 700; font-size: 22px; }

  .section-tab {
    position: absolute; left: 148px; top: 222px; width: 328px; height: 44px;
    border-radius: 0 0 14px 14px;
    background: linear-gradient(var(--tab-silver-top), var(--tab-silver-bottom));
    color: var(--tab-text); font-size: 27px; font-weight: 400; text-align: center; line-height: 44px;
    box-shadow: 0 2px 4px rgba(0,0,0,0.6);
    z-index: 2;
  }

  /* List */
  .restaurant-list {
    position: absolute; left: 0; top: 274px; width: 630px; height: 571px;
    overflow: hidden; list-style: none;
  }
  .restaurant-row {
    position: relative; height: 157px;
    border-top: 1px solid var(--divider);
    background: repeating-linear-gradient(135deg, rgba(255,255,255,0.03) 0 2px, transparent 2px 6px);
  }
  .thumb {
    position: absolute; left: 27px; top: 14px; width: 120px; height: 120px;
    border: 3px solid #ffffff; box-shadow: 0 2px 5px rgba(0,0,0,0.6);
  }
  .thumb-wine { background: linear-gradient(120deg, #c4a56a, #6a1a1a 45%, #d6c35a 70%, #3a2a14); }
  .thumb-burger { background: linear-gradient(160deg, #3c2a1c, #c08a3c 40%, #e2c06a 55%, #5a3a1c 80%, #2a1a10); }
  .ribbon {
    position: absolute; left: 148px; top: 28px; width: 460px; height: 87px;
  }
  .ribbon svg { position: absolute; inset: 0; }
  .ribbon-name {
    position: absolute; left: 37px; top: 14px; color: var(--ribbon-text);
    font-size: 29px; font-weight: 400; text-shadow: 0 1px 1px rgba(0,0,0,0.3);
  }
  .ribbon-cuisine {
    position: absolute; left: 37px; top: 50px; color: var(--ribbon-sub);
    font-size: 21px; font-style: italic;
  }

  /* Tab bar */
  .tab-bar {
    position: absolute; left: 0; top: 845px; width: 630px; height: 90px;
    background: linear-gradient(#2a1a10 0 45%, var(--bar-orange-dark) 45%, var(--bar-orange) 100%);
    display: flex;
  }
  .tab-item {
    flex: 1; position: relative;
    border-right: 1px solid rgba(0,0,0,0.35);
  }
  .tab-item:last-child { border-right: none; }
  .tab-item .tab-shape { position: absolute; top: -5px; left: 50%; margin-left: -58px; }
  .tab-item .tab-icon { position: absolute; top: 6px; left: 50%; margin-left: -13px; }
  .tab-label {
    position: absolute; left: 0; right: 0; top: 40px; text-align: center;
    color: #ffffff; font-size: 15px;
    text-shadow: 0 1px 1px rgba(0,0,0,0.6);
  }
</style>
</head>
<body>
<main class="app-screen">
  <header class="header">
    <div class="status-bar">
      <svg width="40" height="18" viewBox="0 0 40 18" aria-label="Signal">
        <rect x="0" y="13" width="5" height="5" fill="#9a8a80"/>
        <rect x="7" y="10" width="5" height="8" fill="#9a8a80"/>
        <rect x="14" y="7" width="5" height="11" fill="#9a8a80"/>
        <rect x="21" y="4" width="5" height="14" fill="#9a8a80"/>
        <rect x="28" y="1" width="5" height="17" fill="#9a8a80"/>
      </svg>
      <svg width="20" height="24" viewBox="0 0 20 24" aria-label="Verrouillé">
        <path d="M5 10 V7 a5 5 0 0 1 10 0 V10" fill="none" stroke="#9a8a80" stroke-width="3"/>
        <rect x="2" y="10" width="16" height="13" rx="2" fill="#9a8a80"/>
      </svg>
      <svg width="42" height="18" viewBox="0 0 42 18" aria-label="Batterie">
        <rect x="1" y="1" width="36" height="16" rx="3" fill="none" stroke="#9a8a80" stroke-width="2"/>
        <rect x="4" y="4" width="30" height="10" fill="#9a8a80"/>
        <rect x="38" y="6" width="3" height="6" fill="#9a8a80"/>
      </svg>
    </div>
    <div class="range-panel">
      <p class="range-label">12 restaurants dans mon environement</p>
      <div class="range-track"><span class="range-thumb"></span></div>
    </div>
    <div class="brand">
      <span class="brand-dot"></span>
      <span class="brand-name">Dishcart</span>
    </div>
  </header>

  <h1 class="section-tab">Restaurants</h1>

  <ul class="restaurant-list">
    <li class="restaurant-row">
      <div class="thumb thumb-wine" role="img" aria-label="Photo de verres et bouteilles de vin"></div>
      <div class="ribbon">
        <svg width="460" height="87" viewBox="0 0 460 87">
          <defs><linearGradient id="rb1" x1="0" x2="1"><stop offset="0" stop-color="#8f5a2e"/><stop offset="1" stop-color="#c88f58"/></linearGradient></defs>
          <path d="M0 0 H420 L460 43.5 L420 87 H0 Z" fill="url(#rb1)"/>
          <circle cx="410" cy="43.5" r="15" fill="#3b2a20"/>
          <path d="M405 35 L418 43.5 L405 52 Z" fill="#c9b8a8"/>
        </svg>
        <span class="ribbon-name">BELLA LUNA</span>
        <span class="ribbon-cuisine">Italien</span>
      </div>
    </li>
    <li class="restaurant-row">
      <div class="thumb thumb-burger" role="img" aria-label="Photo d'un burger garni"></div>
      <div class="ribbon">
        <svg width="460" height="87" viewBox="0 0 460 87">
          <path d="M0 0 H420 L460 43.5 L420 87 H0 Z" fill="url(#rb1)"/>
          <circle cx="410" cy="43.5" r="15" fill="#3b2a20"/>
          <path d="M405 35 L418 43.5 L405 52 Z" fill="#c9b8a8"/>
        </svg>
        <span class="ribbon-name">Burger Ridge</span>
        <span class="ribbon-cuisine">American</span>
      </div>
    </li>
    <li class="restaurant-row">
      <div class="thumb thumb-wine" role="img" aria-label="Photo de verres et bouteilles de vin"></div>
      <div class="ribbon">
        <svg width="460" height="87" viewBox="0 0 460 87">
          <path d="M0 0 H420 L460 43.5 L420 87 H0 Z" fill="url(#rb1)"/>
          <circle cx="410" cy="43.5" r="15" fill="#3b2a20"/>
          <path d="M405 35 L418 43.5 L405 52 Z" fill="#c9b8a8"/>
        </svg>
        <span class="ribbon-name">BELLA LUNA</span>
        <span class="ribbon-cuisine">Italien</span>
      </div>
    </li>
    <li class="restaurant-row">
      <div class="thumb thumb-burger" role="img" aria-label="Photo d'un burger garni"></div>
      <div class="ribbon">
        <svg width="460" height="87" viewBox="0 0 460 87">
          <path d="M0 0 H420 L460 43.5 L420 87 H0 Z" fill="url(#rb1)"/>
          <circle cx="410" cy="43.5" r="15" fill="#3b2a20"/>
          <path d="M405 35 L418 43.5 L405 52 Z" fill="#c9b8a8"/>
        </svg>
        <span class="ribbon-name">Burger Ridge</span>
        <span class="ribbon-cuisine">American</span>
      </div>
    </li>
  </ul>

  <nav class="tab-bar">
    <div class="tab-item">
      <svg class="tab-shape" width="116" height="86" viewBox="0 0 116 86"><path d="M4 0 H112 L110 62 L70 66 L58 82 L46 66 L6 62 Z" fill="#6e4635" stroke="#4e3022" stroke-width="2"/></svg>
      <svg class="tab-icon" width="26" height="26" viewBox="0 0 26 26"><circle cx="11" cy="11" r="7" fill="none" stroke="#fff" stroke-width="3"/><path d="M16 16 L23 23" stroke="#fff" stroke-width="4" stroke-linecap="round"/></svg>
      <span class="tab-label">CHERCHER</span>
    </div>
    <div class="tab-item">
      <svg class="tab-shape" width="116" height="86" viewBox="0 0 116 86"><path d="M4 0 H112 L110 62 L70 66 L58 82 L46 66 L6 62 Z" fill="#6e4635" stroke="#4e3022" stroke-width="2"/></svg>
      <svg class="tab-icon" width="26" height="26" viewBox="0 0 26 26"><circle cx="13" cy="13" r="12" fill="#fff"/><rect x="11" y="5" width="4" height="10" fill="#6e4635"/><rect x="11" y="17" width="4" height="4" fill="#6e4635"/></svg>
      <span class="tab-label">COMMANDES</span>
    </div>
    <div class="tab-item">
      <svg class="tab-shape" width="116" height="86" viewBox="0 0 116 86"><path d="M4 0 H112 L110 62 L70 66 L58 82 L46 66 L6 62 Z" fill="#6e4635" stroke="#4e3022" stroke-width="2"/></svg>
      <svg class="tab-icon" width="26" height="26" viewBox="0 0 26 26"><circle cx="13" cy="8" r="6" fill="#fff"/><path d="M2 26 C2 16 24 16 24 26 Z" fill="#fff"/></svg>
      <span class="tab-label">COMPTE</span>
    </div>
  </nav>
</main>
</body>
</html>
```